Webdesign für Gemeinschaftspraxis (13820)
Zielgruppe
Die Website ist für eine fachärztliche Gemeinschaftspraxis, die sich aus Internisten, Betriebsmedizinern, Präventionsärzten, Kardiologen, Allgemeinmedizinern und Phlebologen zusammensetzt.
Die Zielgruppe sind bestehende Patienten sowie potentielle Patienten.
Die Website soll informativ sein.
Aufgabenstellung
Die Website soll in schlichten Farben gehalten sein, die zum Logo und zu den Fotos passen.
Die Website soll als kurzer, informativer Auftritt dienen
Die gelieferten Fotos sollen verwendet werden.
Es soll eine Onepage-Website werden, die so aufgebaut ist, wie die Website unter dem folgenden Link: https://www.kolbenfeld-portal.de/

```html
<!DOCTYPE html>
<html lang="de">
<head>
<meta charset="utf-8">
<title>Gemeinschaftspraxis Marlbach</title>
<link href="https://fonts.googleapis.com/css2?family=Karla:ital,wght@0,300;0,400;0,500;0,700;1,400&display=swap" rel="stylesheet">
<style>
:root{
  --navy:#1c2b5a;
  --navy-2:#2f4a8a;
  --navy-strip:#3c5aa0;
  --accent:#5d7bc8;
  --light:#f8f8fa;
  --text:#4a4f60;
  --th:#3a5bb8;
  --time:#6d8ad9;
  --purple:#b862cc;
  --free:#8da1bd;
  --house:#e8979a;
  --lunch:#687aa0;
  --appoint:#819cd6;
  --green:#72c3a1;
  --btn:#7d9bd5;
}
*{box-sizing:border-box;margin:0;padding:0}
html,body{width:1200px;height:3723px;overflow:hidden}
body{font-family:"Karla",sans-serif;color:var(--text);background:#fff;position:relative}
section,header,footer{position:absolute;left:0;width:1200px}

/* Hero */
.hero{top:0;height:630px;overflow:hidden}
.hero-photo{position:absolute;inset:0;background:linear-gradient(115deg,#e9ecef 0%,#f4f1ec 35%,#d9c3a2 55%,#efeae3 70%,#c9c6c2 100%)}
.hero-shape{position:absolute;inset:0}
.logo{position:absolute;left:111px;top:17px;width:232px;height:132px;background:#fff;display:flex;align-items:center;justify-content:center;gap:10px;flex-direction:column}
.logo-name{font-weight:700;font-size:17px;color:var(--navy);letter-spacing:.5px;text-align:center;line-height:1.2}
.logo-sub{font-size:9px;color:var(--navy)}
.nav{position:absolute;right:0;top:0;width:692px;height:84px;background:var(--navy);display:flex;align-items:center;padding-left:47px;gap:31px}
.nav a{color:#fff;text-decoration:none;font-weight:700;font-size:11px;letter-spacing:.6px}
.hero-band{position:absolute;left:564px;top:445px;width:636px;height:93px;background:rgba(255,255,255,.55)}
.hero-title{position:absolute;right:110px;top:448px;text-align:right;color:var(--navy)}
.hero-title h1{font-size:42px;font-weight:700;letter-spacing:1px;line-height:1}
.hero-title p{font-size:30px;font-weight:400;letter-spacing:1px;line-height:1.1;margin-top:4px}

/* Section headings */
.section-title{position:absolute;left:0;width:1200px;text-align:center;font-weight:400;color:var(--navy);font-size:32px;letter-spacing:1.5px}

/* Services */
.services{top:630px;height:748px;background:var(--light)}
.services .section-title{top:78px}
.services-intro{position:absolute;left:0;width:1200px;top:126px;text-align:center;font-style:italic;font-size:14.5px;line-height:22px;color:var(--text)}
.service-menu{position:absolute;left:111px;top:206px;width:318px;height:454px;background:var(--navy)}
.service-menu ul{list-style:none;width:308px}
.service-menu li{height:62px;border-bottom:1px solid #33467a;color:#d6def2;font-weight:700;font-size:12.5px;letter-spacing:.5px;display:flex;align-items:center;padding:0 12px}
.service-menu li.first{height:84px;line-height:22px}
.service-menu li.active{background:var(--navy-2);color:#fff}
.menu-scroll{position:absolute;left:308px;top:72px;width:10px;height:200px;background:var(--navy-strip)}
.service-panel{position:absolute;left:429px;top:206px;width:658px;height:454px;background:#fff;border:1.5px solid var(--navy);padding:32px 26px}
.service-top{display:flex;justify-content:space-between;align-items:flex-start;height:233px;margin-bottom:9px}
.service-top-text{width:350px}
.service-panel h3{color:var(--navy);font-size:17px;font-weight:700;letter-spacing:.5px;margin-bottom:12px}
.service-panel p{font-size:12.6px;line-height:22px;color:var(--text)}
.service-panel .gap{margin-top:22px}
.service-photo{flex:none;width:233px;height:204px;margin-top:3px;background:linear-gradient(120deg,#e9dcc8 0%,#f3ede4 45%,#2d58b5 75%,#1e3f8e 100%)}

/* Doctors */
.doctors{top:1378px;height:607px;background:#fff}
.doctors .section-title{top:52px}
.doctor{position:absolute;top:119px;width:308px;height:412px;background:#fff;box-shadow:0 2px 14px rgba(28,43,90,.09);text-align:center}
.doctor-photo{margin:42px auto 0;width:136px;height:136px;border:1.5px solid #4fb4d8;padding:6px}
.doctor-photo div{width:100%;height:100%;background:linear-gradient(160deg,#d8dbe0,#9a8f88 60%,#4b4a4f)}
.doctor h4{margin-top:22px;font-size:16.5px;font-weight:500;color:#2b2f3b}
.doctor .role{font-size:11px;color:#9aa0ac;margin-top:4px;letter-spacing:.5px}
.doctor p{font-size:13px;line-height:22px;margin:18px 40px 0;color:var(--text)}

/* Hours */
.hours{top:1985px;height:904px;overflow:hidden}
.hours-bg{position:absolute;inset:0;background:linear-gradient(90deg,#d9dde5 0%,#eef0f4 30%,#f4f5f8 60%,#dfe2e8 100%)}
.hours .section-title{top:46px;color:#3b5bb0}
.timetable{position:absolute;left:111px;top:99px;width:976px;border-collapse:collapse;table-layout:fixed}
.timetable th,.timetable td{border:1px solid rgba(255,255,255,.45);text-align:left;vertical-align:top;color:#fff;font-weight:700;font-size:14px;line-height:19px;padding:14px 17px 0}
.timetable th{background:var(--th);height:42px;padding-top:12px;font-size:13.5px;letter-spacing:.5px;padding-left:24px}
.timetable td{height:64.2px}
.timetable td.time{background:var(--time);padding-left:22px}
.c-blood{background:var(--purple)}
.c-free{background:var(--free)}
.c-house{background:var(--house);font-weight:500!important}
.c-lunch{background:var(--lunch)}
.c-appoint{background:var(--appoint)}
.c-green{background:var(--green)}
.c-empty{background:rgba(220,224,232,.6)}

/* Team */
.team{top:2889px;height:480px;background:#fff}
.team-photo{position:absolute;left:116px;top:20px;width:585px;height:460px;background:linear-gradient(180deg,#f1f3f6 0%,#e6e9ee 40%,#2f6bc4 80%,#2756a8 100%);clip-path:polygon(8% 25%,20% 8%,40% 0,60% 4%,80% 6%,95% 30%,100% 100%,0 100%)}
.team-text{position:absolute;left:724px;top:90px;width:362px}
.team-text h2{font-size:31px;font-weight:400;color:var(--navy);letter-spacing:1px;margin-bottom:14px}
.team-text p{font-size:12.5px;line-height:22px;color:var(--text)}
.team-text p+p{margin-top:22px}

/* Footer */
.footer{top:3369px;height:354px;background:var(--navy)}
.footer h2{position:absolute;top:66px;font-size:31px;font-weight:300;color:var(--accent);letter-spacing:1px}
.contact-list{position:absolute;left:111px;top:140px;width:480px;font-size:12px;color:#5f76b6}
.contact-item{position:absolute;display:flex;align-items:center;gap:8px;white-space:nowrap}
.contact-item svg{width:12px;height:12px;flex:none}
.form{position:absolute;left:613px;top:123px;width:474px}
.field{position:absolute;height:49px;background:#283b70;color:#6279b8;font-style:italic;font-size:12px;padding:16px 16px}
.submit{position:absolute;left:0;top:116px;width:474px;height:49px;background:var(--btn);color:var(--navy);font-weight:500;font-size:13.5px;letter-spacing:2px;text-align:center;line-height:49px}
</style>
</head>
<body>

<header class="hero">
  <div class="hero-photo" role="img" aria-label="Foto des hellen Empfangsbereichs der Praxis mit Holztresen und Gang"></div>
  <svg class="hero-shape" width="1200" height="630" viewBox="0 0 1200 630" aria-hidden="true">
    <polygon points="0,0 470,0 0,200" fill="#f2f3f5" opacity=".55"/>
    <polygon points="0,190 0,630 500,630" fill="#1c2b5a"/>
  </svg>
  <div class="logo">
    <div class="logo-name">Gemeinschaftspraxis<br>Marlbach</div>
    <div class="logo-sub">Dr. Hollberg · Dr. Wendt · Kaspers</div>
  </div>
  <nav class="nav">
    <a href="#">HOME</a>
    <a href="#">DIENSTLEISTUNGEN</a>
    <a href="#">UNSER TEAM</a>
    <a href="#">ÖFFNUNGSZEITEN</a>
    <a href="#">KONTAKTIERE UNS</a>
  </nav>
  <div class="hero-band"></div>
  <div class="hero-title">
    <h1>SED UT PERSPICIATIS</h1>
    <p>UNDE OMNIS ISTE NATUS</p>
  </div>
</header>

<section class="services">
  <h2 class="section-title">UNSERE DIENSTLEISTUNGEN</h2>
  <p class="services-intro">Nemo enim ipsam voluptatem quia voluptas sit aspernatur aut odit aut fugit, sed quia<br>consequuntur magni dolores eos qui ratione voluptatem sequi nesciunt.</p>
  <div class="service-menu">
    <ul>
      <li class="first">GESUNDHEITSVORSORGE<br>/PRÄVENTION/ GESUNDHEITS-CHECK-UP</li>
      <li>IMPFUNGEN UND REISEIMPFUNGEN</li>
      <li class="active">MÄNNERVORSORGE</li>
      <li>DIABETES MELLITUS</li>
      <li>PSYCHOSOMATISCHE GRUNDVERSORGUNG</li>
      <li>KORONARE HERZERKRANKUNG (KHK)</li>
      <li>ASTHMA BRONCHIAL</li>
    </ul>
    <div class="menu-scroll"></div>
  </div>
  <div class="service-panel">
    <div class="service-top">
      <div class="service-top-text">
        <h3>MÄNNERVORSORGE</h3>
        <p>Sed ut perspiciatis unde omnis iste natus error sit voluptatem accusantium doloremque laudantium, totam rem aperiam, eaque ipsa quae ab illo inventore veritatis et quasi architecto beatae vitae dicta sunt explicabo. Nemo enim ipsam voluptatem quia voluptas sit aspernatur aut odit aut fugit, sed quia consequuntur magni dolores eos qui ratione voluptatem sequi nesciunt.</p>
      </div>
      <div class="service-photo" role="img" aria-label="Foto einer Ärztin im Gespräch mit einem Patienten am Empfang"></div>
    </div>
    <p>Qui dolorem ipsum quia dolor sit amet, consectetur, adipisci velit, sed quia non numquam eius modi tempora incidunt ut labore et dolore magnam aliquam quaerat voluptatem.</p>
    <p class="gap">Ut enim ad minima veniam, quis nostrum exercitationem ullam corporis suscipit laboriosam, nisi ut aliquid ex ea commodi consequatur? Quis autem vel eum iure reprehenderit qui in ea voluptate velit esse quam nihil molestiae consequatur, vel illum qui dolorem eum fugiat quo voluptas nulla pariatur.</p>
  </div>
</section>

<section class="doctors">
  <h2 class="section-title">UNSERE ÄRZTE</h2>
  <article class="doctor" style="left:111px">
    <div class="doctor-photo"><div role="img" aria-label="Porträtfoto von Lena Ortmann"></div></div>
    <h4>Lena Ortmann</h4><div class="role">Vice President</div>
    <p>Neque porro quisquam est, qui dolorem ipsum quia dolor sit amet, consectetur, adipisci velit, sed quia non numquam eius modi tempora incidunt ut labore et dolore.</p>
  </article>
  <article class="doctor" style="left:445px">
    <div class="doctor-photo"><div role="img" aria-label="Porträtfoto von Felix Brandt"></div></div>
    <h4>Felix Brandt</h4><div class="role">Vice President</div>
    <p>Neque porro quisquam est, qui dolorem ipsum quia dolor sit amet, consectetur, adipisci velit, sed quia non numquam eius modi tempora incidunt ut labore et dolore.</p>
  </article>
  <article class="doctor" style="left:779px">
    <div class="doctor-photo"><div role="img" aria-label="Porträtfoto von Jonas Keller"></div></div>
    <h4>Jonas Keller</h4><div class="role">Vice President</div>
    <p>Neque porro quisquam est, qui dolorem ipsum quia dolor sit amet, consectetur, adipisci velit, sed quia non numquam eius modi tempora incidunt ut labore et dolore.</p>
  </article>
</section>

<section class="hours">
  <div class="hours-bg" role="img" aria-label="Blasses Foto des Praxisgebäudes mit Bäumen im Hintergrund"></div>
  <h2 class="section-title">ÖFFNUNGSZEITEN</h2>
  <table class="timetable">
    <thead><tr><th>ZEIT</th><th>MONTAG</th><th>DIENSTAG</th><th>MITTWOCH</th><th>DONNERSTAG</th><th>FREITAG</th></tr></thead>
    <tbody>
      <tr><td class="time">AB 7:30</td><td class="c-blood">Blutentnahme/ Ultraschall</td><td class="c-blood">Blutentnahme/ Ultraschall</td><td class="c-blood">Blutentnahme/ Ultraschall</td><td class="c-blood">Blutentnahme/ Ultraschall</td><td class="c-blood">Blutentnahme/ Ultraschall</td></tr>
      <tr><td class="time">8:00-9:30</td><td class="c-free">Freie Sprechstunde</td><td class="c-free">Freie Sprechstunde</td><td class="c-free">Freie Sprechstunde</td><td class="c-free">Freie Sprechstunde</td><td class="c-free">Freie Sprechstunde</td></tr>
      <tr><td class="time">9:00-10:00</td><td class="c-free">Freie Sprechstunde</td><td class="c-free">Freie Sprechstunde</td><td class="c-free">Freie Sprechstunde</td><td class="c-free">Freie Sprechstunde</td><td class="c-free">Freie Sprechstunde</td></tr>
      <tr><td class="time">10:00-11:00</td><td class="c-free">Freie Sprechstunde</td><td class="c-free">Freie Sprechstunde</td><td class="c-free">Freie Sprechstunde</td><td class="c-free">Freie Sprechstunde</td><td class="c-free">Freie Sprechstunde</td></tr>
      <tr><td class="time">11:00-12:00</td><td class="c-free">Freie Sprechstunde</td><td class="c-free">Freie Sprechstunde</td><td class="c-free">Freie Sprechstunde</td><td class="c-free">Freie Sprechstunde</td><td class="c-free">Freie Sprechstunde</td></tr>
      <tr><td class="time">12:00-13:00</td><td class="c-house">Hausbesuche</td><td class="c-house">Hausbesuche</td><td class="c-house">Hausbesuche</td><td class="c-house">Hausbesuche</td><td class="c-house">Hausbesuche</td></tr>
      <tr><td class="time">13:00-14:00</td><td class="c-lunch">Mittagspause</td><td class="c-lunch">Mittagspause</td><td class="c-lunch">Mittagspause</td><td class="c-lunch">Mittagspause</td><td class="c-lunch">Mittagspause</td></tr>
      <tr><td class="time">14:00-15:30</td><td class="c-lunch">Mittagspause</td><td class="c-lunch">Mittagspause</td><td class="c-lunch">Mittagspause</td><td class="c-lunch">Mittagspause</td><td class="c-lunch">Mittagspause</td></tr>
      <tr><td class="time">15:30-16:00</td><td class="c-appoint">Termin-<br>sprechstunde</td><td class="c-appoint">Termin-<br>sprechstunde</td><td class="c-appoint">Termin-<br>sprechstunde</td><td class="c-appoint">Termin-<br>sprechstunde</td><td class="c-appoint">Termin-<br>sprechstunde</td></tr>
      <tr><td class="time">16:00-17:00</td><td class="c-green">Freie Sprechstunde</td><td class="c-green">Freie Sprechstunde</td><td class="c-empty"></td><td class="c-green">Freie Sprechstunde</td><td class="c-empty"></td></tr>
      <tr><td class="time">17:00-18:00</td><td class="c-green">Freie Sprechstunde</td><td class="c-green">Freie Sprechstunde</td><td class="c-empty"></td><td class="c-green">Freie Sprechstunde</td><td class="c-empty"></td></tr>
    </tbody>
  </table>
</section>

<section class="team">
  <div class="team-photo" role="img" aria-label="Gruppenfoto des Praxisteams in weißen Kitteln und blauer Kleidung"></div>
  <div class="team-text">
    <h2>TRIFF DAS TEAM</h2>
    <p>But I must explain to you how all this mistaken idea of denouncing pleasure and praising pain was born and I will give you a complete account of the system, and expound the actual teachings of the great explorer of the truth, the master-builder of human happiness.</p>
    <p>No one rejects, dislikes, or avoids pleasure itself, because it is pleasure, but because those who do not know how to pursue pleasure rationally encounter consequences that are extremely painful.</p>
  </div>
</section>

<footer class="footer">
  <h2 style="left:111px">SCHNELLER KONTAKT</h2>
  <h2 style="left:692px">KONTAKT FORMULAR</h2>
  <div class="contact-list">
    <div class="contact-item" style="left:0;top:0">
      <svg viewBox="0 0 12 12"><path d="M6 0.5a4 4 0 0 0-4 4c0 3 4 7 4 7s4-4 4-7a4 4 0 0 0-4-4zm0 5.6a1.6 1.6 0 1 1 0-3.2 1.6 1.6 0 0 1 0 3.2z" fill="#5f76b6"/></svg>
      Am Lindenhof 7, 48210 Marlbach</div>
    <div class="contact-item" style="left:0;top:26px">
      <svg viewBox="0 0 12 12"><rect x="1" y="3" width="10" height="6" fill="#5f76b6"/><rect x="3" y="1" width="6" height="2" fill="#5f76b6"/></svg>
      04417 239185</div>
    <div class="contact-item" style="left:269px;top:0">
      <svg viewBox="0 0 12 12"><circle cx="6" cy="6" r="5.2" fill="none" stroke="#5f76b6" stroke-width="1.2"/><path d="M4 3.5l1 1.3-.6.8c.5 1 1.1 1.6 2 2l.8-.6 1.3 1-.8 1c-2.2-.4-3.9-2.1-4.3-4.3z" fill="#5f76b6"/></svg>
      04417 239184</div>
    <div class="contact-item" style="left:269px;top:26px">
      <svg viewBox="0 0 12 12"><rect x="1" y="2.5" width="10" height="7" fill="none" stroke="#5f76b6" stroke-width="1.2"/><path d="M1 2.5l5 4 5-4" fill="none" stroke="#5f76b6" stroke-width="1.2"/></svg>
      info@praxis-marlbach.de</div>
    <div class="contact-item" style="left:1px;top:62px">Copyright © 2019. Gemeinschaftspraxis Marlbach</div>
    <div class="contact-item" style="left:295px;top:62px">Datenschutz-Bestimmungen</div>
    <div class="contact-item" style="left:1px;top:88px">Alle Rechte vorbehalten.</div>
  </div>
  <div class="form">
    <div class="field" style="left:0;top:0;width:233px">Name:</div>
    <div class="field" style="left:241px;top:0;width:233px">Telefon:</div>
    <div class="field" style="left:0;top:58px;width:474px">Email:</div>
    <div class="submit">EINREICHEN</div>
  </div>
</footer>

</body>
</html>
```